Sharp, new and modern business flyer

We are an industrial crate manufacturer whose core customer base is in the aeronautical parts sector. We also however build very custom travel show crates and road cases for any spectrum of industries. We have a substantial facility and can accommodate large, production orders so we would like to attract large, local businesses if possible, but ship crates nationwide as well. We have an old tri fold flyer that we have been using for over 3+ years that I will attach for reference but it desperately needs a fresh new look and complete revamp! Our slogan is "Innovative Crating With Superior Service." We are known in the industry as being extremely fast as well as providing excellent customer service and crate design work. We have also in the last year, added two globes to the background of our logo. I am attaching our current business cards that show how we incorporate that. Feel free to visit our website as well as our Facebook page for more info and current pictures. Both are Palbrook-freight.com.

Target Market(s)

Mid to large local business and corporations. Industrial and manufacturing - especially aeronautical or medical (delicate surgical equipment) as well as military.

Industry/Entity Type

Manufacturer

Font styles to use
Sans Serif
Other font styles liked:
• Stencil

Colors

Designer to choose colors to be used in the design.

Requirements
Must have
• 1. Current photos and descriptions of our capabilities. Our most current products are on our Facebook page and our capabilities are on our website.
• 2. Our flyer must state that "All of our quality products are built with lumber that is ISPM 15 Heat Treatment Certified"
• 3. Please add custom pallets as well as on-site crating
Nice to have
• A new, modern look that shows us as current and growing.
Should not have
• Woman owned listed...we are no longer woman owned.

```html
<!DOCTYPE html>
<html lang="en">
<head>
<meta charset="utf-8">
<title>Palbrook-freight.com Tri-fold</title>
<link rel="stylesheet" href="https://fonts.googleapis.com/css2?family=Bebas+Neue&family=Lato:wght@400;700&display=swap">
<style>
  :root {
    --page: #e6e6e6;
    --paper: #ffffff;
    --paper-shade: #ececec;
    --amber: #e8ad4f;
    --amber-deep: #e0a13c;
    --ink: #1c1c1c;
    --text: #222;
  }
  * { box-sizing: border-box; margin: 0; padding: 0; }
  html, body { width: 1200px; height: 1200px; overflow: hidden; background: var(--page); }
  .brochure {
    position: absolute; left: 0; top: 173px; width: 1200px; height: 854px;
    font-family: "Lato", sans-serif; color: var(--text);
  }
  .panel { position: absolute; top: 0; height: 854px; }
  .panel--left { left: 0; width: 407px; background: linear-gradient(90deg, var(--paper) 60%, var(--paper-shade)); }
  .panel--middle { left: 407px; width: 395px; background: var(--amber); }
  .panel--right { left: 802px; width: 398px; background: linear-gradient(90deg, var(--paper-shade), var(--paper) 40%); }
  .abs { position: absolute; }
  .backing { background: var(--amber); }
  .photo { box-shadow: 0 2px 6px rgba(0,0,0,.3); }
  .photo--warehouse { background: linear-gradient(180deg, #c9b48c 0%, #b9a27a 45%, #8e8d8b 100%); }
  .photo--aisle { background: linear-gradient(180deg, #b0865a 0%, #c8a777 40%, #5f5f5f 100%); }
  .photo--crate { background: linear-gradient(160deg, #d8b788 0%, #c9a06c 55%, #a8865a 100%); }
  .photo--hero { background: linear-gradient(140deg, #e6cfa4 0%, #d6b07a 60%, #b58f5d 100%); }
  .photo--framed { border: 2px solid var(--ink); }
  .heading {
    font-family: "Bebas Neue", sans-serif; color: var(--ink);
    letter-spacing: .5px; line-height: 1;
  }
  .section-title { font-size: 29px; }
  .body-copy { font-size: 13.2px; line-height: 1.3; }
  .justify { text-align: justify; }
  .services { font-size: 21px; text-align: center; width: 395px; left: 0; }
  .certified { font-size: 12.5px; line-height: 1.3; text-align: center; color: var(--ink); left: 30px; width: 338px; }
  .certified strong { font-weight: 700; }
  .brand-mark { display: flex; align-items: center; justify-content: center; gap: 6px; font-weight: 700; color: var(--ink); }
  .brand-mark__square { background: var(--ink); flex: none; }
  .contact-row { display: flex; align-items: center; gap: 10px; font-size: 16px; color: var(--ink); }
  .contact-row svg { width: 18px; height: 18px; flex: none; }
  .web-pill {
    border-radius: 18px; display: flex; align-items: center; justify-content: center;
    font-weight: 700; font-size: 18px; color: var(--ink);
  }
  .web-pill--light { background: var(--paper); }
  .web-pill--amber { background: var(--amber); }
  .headline { font-size: 43px; text-align: center; left: 0; width: 398px; }
  .headline--accent { color: var(--amber-deep); }
</style>
</head>
<body>
<main class="brochure">

  <section class="panel panel--left">
    <div class="abs backing" style="left:49px;top:23px;width:243px;height:203px"></div>
    <div class="abs photo photo--warehouse" style="left:87px;top:32px;width:245px;height:185px" role="img" aria-label="Photo of stacked collapsible crate panels on warehouse racks with an assembled crate in front"></div>
    <h2 class="abs heading section-title" style="left:50px;top:258px">Collapsible Crates</h2>
    <p class="abs body-copy" style="left:54px;top:299px;width:300px">Our custom collapsible and reusable crates use a latch-ing system. perfect for trade shows and for storage, these collapsible crates are very durable, cost effective and easy to store.</p>

    <div class="abs backing" style="left:106px;top:393px;width:237px;height:203px"></div>
    <div class="abs photo photo--aisle" style="left:74px;top:407px;width:240px;height:180px" role="img" aria-label="Photo of a long flat crate on a pallet in a warehouse aisle lined with boxes"></div>
    <h2 class="abs heading section-title" style="left:48px;top:630px">Corrugated Boxes</h2>
    <p class="abs body-copy justify" style="left:51px;top:670px;width:296px">We are pleased to announce that we now offer corru-gated boxes. They are light weight but heavy duty and help reduce shipping costs. Fully customizable to nearly any size, we offer singe, double or tri-wall card-board as well as wood pallet bases for ease of trans-portation for heavi-er boxes. We also have standard size, fully col-lapsible bulk shipping kits ready for you to unfold and load for shipping.</p>
  </section>

  <section class="panel panel--middle">
    <h2 class="abs heading" style="left:21px;top:24px;font-size:32px">Our History</h2>
    <p class="abs body-copy justify" style="left:19px;top:64px;width:339px">Our incredible story began in 2006, with little more than $200 in our pocket, we started building shipping crates in our garage, and made deliveries using the family SUV. Years of hard work and extreme determination have resulted in tremendous growth. We now have state of the art design software as well as a full staff of skilled carpenters and craftsman meticulously filling every order from our newly expanded production facility. We are still hands-on from the time a crate is designed to the minute that it ships.</p>

    <div class="abs photo photo--crate photo--framed" style="left:24px;top:262px;width:170px;height:127px" role="img" aria-label="Photo of long wooden crates stacked on pallets"></div>
    <div class="abs photo photo--crate photo--framed" style="left:200px;top:262px;width:170px;height:127px" role="img" aria-label="Photo of an open-top wooden crate on a shop floor"></div>
    <div class="abs photo photo--crate photo--framed" style="left:22px;top:422px;width:172px;height:124px" role="img" aria-label="Photo of several wooden crates in a production facility"></div>
    <div class="abs photo photo--crate photo--framed" style="left:200px;top:422px;width:172px;height:124px" role="img" aria-label="Photo of stacked wooden crates with metal latches"></div>

    <p class="abs heading services" style="top:560px">Custom Pallets &nbsp;•&nbsp; On-Site Crating</p>

    <div class="abs brand-mark" style="left:100px;top:604px;width:195px;font-size:14px">
      <span class="brand-mark__square" style="width:12px;height:12px"></span>Palbrook-freight.com
    </div>

    <div class="abs contact-row" style="left:37px;top:670px">
      <svg viewBox="0 0 20 20" fill="none" stroke="#1c1c1c" stroke-width="1.6"><path d="M10 18s-6-6-6-10a6 6 0 0 1 12 0c0 4-6 10-6 10z"/><circle cx="10" cy="8" r="2.2"/></svg>
      <span>4180 West Marlow Avenue Dania, Fl 33004</span>
    </div>
    <div class="abs contact-row" style="left:37px;top:697px">
      <svg viewBox="0 0 20 20" fill="none" stroke="#1c1c1c" stroke-width="1.6"><circle cx="10" cy="10" r="8.5"/><path d="M7 5.5l1.6 2.3-1 1.2a6 6 0 0 0 3.4 3.4l1.2-1 2.3 1.6-1 1.5c-3.8 0-7.5-3.7-7.5-7.5z"/></svg>
      <span>954-555-0142</span>
    </div>
    <div class="abs contact-row" style="left:37px;top:724px">
      <svg viewBox="0 0 20 20" fill="none" stroke="#1c1c1c" stroke-width="1.6"><rect x="2" y="4.5" width="16" height="11"/><path d="M2 4.5l8 6.5 8-6.5M2 15.5l6-5M18 15.5l-6-5"/></svg>
      <span>dana@palbrook-freight.com</span>
    </div>

    <div class="abs web-pill web-pill--light" style="left:41px;top:773px;width:305px;height:34px">www.palbrook-freight.com</div>
  </section>

  <section class="panel panel--right">
    <div class="abs brand-mark" style="left:0;top:118px;width:398px;font-size:19px">
      <span class="brand-mark__square" style="width:16px;height:16px"></span>Palbrook-freight.com
    </div>

    <h1 class="abs heading headline" style="top:236px">Innovative Crating</h1>
    <p class="abs heading headline headline--accent" style="top:279px">With Superior Service</p>

    <div class="abs photo--hero" style="left:31px;top:364px;width:367px;height:346px;border-radius:2px" role="img" aria-label="Photo of a large plywood shipping crate on a wooden pallet base"></div>

    <p class="abs certified" style="top:724px">All of our quality products are built with lumber that is <strong>ISPM 15 Heat Treatment Certified</strong></p>

    <div class="abs web-pill web-pill--amber" style="left:44px;top:772px;width:304px;height:35px">www.palbrook-freight.com</div>
  </section>

</main>
</body>
</html>
```